Personal coach needs brochure design for inspirational essay about authenticity

Overview:
I want a beautiful brochure, 11”x17” that folds to 8-1/2”x11” with 4 pages. Think of it as an oversize greeting card.
• Front cover: photograph of a dancer and title with attribution of quote (Lumafold jpeg photo attached)
• Inside spread: Copy (Helena Brisk copy attached) with some appropriate illustration, based on cover photo
• Back cover: contact information, brief descriptive copy, two small photos (jpeg photo attached; see copy for direction)
Copy for front cover title, inside spread and back cover is attached in doc titled "Helena Brisk copy"

Purpose of brochure:
I'm a personal coach and once a year I produce a 4-page illustrated inspirational essay, which invites personal reflection on living a more mindful, meaningful life. Most people I send them to collect them. Someday in the future I'd like to put a collection of these essays into a coffee table book and also create a website for the collection, which is related to the personal coaching that I do.
I have the brochures printed hard copy. I have attached a few examples from previous years. Each has a unique design related to its theme.

Concept:
This year’s essay theme, “There will only ever be one you!” is based on a quote by Helena Brisk, a famous modern dancer. The complete quote, which appears in the copy, is about being true to one’s authentic self. The essay is not about dance, but because the author of the quote was a dancer who personified this theme of being unique to self, I have selected a photo of dance for the cover.

Design Guidance:
Front cover: One possibility is to expand the background color of the Lumafold photo so the photo seems to emerge from the background. But I am open to ideas. I think the photo is artsy enough as it is, but there may be other ways to treat it (e.g. special effects) that would also work. The title should appear somewhere. Make the attribution (--Helena Brisk) in smaller type than the title.

Inside Spread: There may be ways to borrow a design motif from the cover photo to make the inside spread more visually interesting, i.e., not just straight copy. I think it may be helpful to make the font size of the quote larger than the rest of the copy, but it has to be read in sequence. Or maybe it's printed in same size as copy, but then also repeated and displayed by itself in larger type.

Back cover: If you look at some of the other examples I’ve sent, you’ll see how the back cover is typically handled. I want a reduced version of the cover to be placed near the line that says "this is the 16th in a series.." Then, there’s a jpeg photo of Helena Brisk that should be placed next to the copy description of her.

Need extra days to review

```html
<!DOCTYPE html>
<html lang="en">
<head>
<meta charset="utf-8">
<title>There Will Only Ever Be One You — Brochure</title>
<link rel="stylesheet" href="https://fonts.googleapis.com/css2?family=Archivo+Black&family=Open+Sans:ital,wght@0,400;0,600;0,700;1,400&family=Sacramento&display=swap">
<style>
  :root {
    --magenta: #d6198a;
    --amber: #f2a516;
    --ink: #1c1c1c;
    --paper: #ffffff;
    --paper-grey: #eeeeee;
    --night: #050505;
    --stage: #d8d8db;
    --denim: #3d5670;
  }
  * { box-sizing: border-box; margin: 0; padding: 0; }
  html, body { width: 1200px; height: 1048px; overflow: hidden; }
  body {
    background: var(--stage);
    font-family: "Open Sans", Arial, sans-serif;
    color: var(--ink);
    position: relative;
  }
  .spread {
    position: absolute;
    left: 210px;
    width: 780px;
    height: 505px;
    display: flex;
    box-shadow: 0 6px 18px rgba(0,0,0,.18);
  }
  .spread--outside { top: 12px; }
  .spread--inside { top: 531px; }
  .page { position: relative; width: 390px; height: 505px; overflow: hidden; }

  /* Back cover */
  .back-cover { background: var(--paper-grey); padding: 34px 30px; font-size: 6.6px; line-height: 1.45; }
  .series { display: flex; gap: 8px; align-items: flex-start; }
  .mini-cover {
    flex: none; width: 48px; height: 48px; background: var(--paper);
    border: 1px solid #cfcfcf; position: relative; overflow: hidden;
  }
  .mini-cover .mini-photo {
    position: absolute; left: 3px; top: 12px; width: 26px; height: 26px;
    background: radial-gradient(ellipse at 50% 50%, #4a6481 0%, #1f2c3a 60%, transparent 72%);
  }
  .mini-cover .mini-title {
    position: absolute; left: 22px; top: 5px; font-family: "Archivo Black", sans-serif;
    font-size: 5px; line-height: .9; color: var(--magenta);
  }
  .mini-cover .mini-you {
    position: absolute; left: 22px; top: 30px; font-family: "Sacramento", cursive;
    font-size: 11px; color: var(--amber);
  }
  .series-intro { font-size: 9px; line-height: 1.25; }
  .series-intro em { color: var(--magenta); font-weight: 700; }
  .contact { margin-top: 4px; font-size: 6.4px; line-height: 1.5; }
  .contact strong { font-weight: 700; }
  .contact .gap { margin-top: 5px; }
  .portrait-small {
    margin: 22px 0 0 36px; width: 58px; height: 42px;
    background: radial-gradient(ellipse at 45% 50%, #bdb4a5 0%, #5a5449 35%, #0d0d0d 70%);
  }
  .about { margin-top: 12px; }
  .about h3 { color: var(--magenta); font-size: 6.8px; font-weight: 700; text-transform: uppercase; }
  .about p { margin-bottom: 6px; }

  /* Front cover */
  .front-cover { background: var(--paper); }
  .dancer-photo {
    position: absolute; left: 50px; top: 92px; width: 250px; height: 300px;
    background: radial-gradient(ellipse 60% 45% at 45% 55%, var(--denim) 0%, #2a3a4c 45%, rgba(255,255,255,0) 75%);
  }
  .cover-title {
    position: absolute; left: 200px; top: 78px;
    font-family: "Archivo Black", sans-serif; font-size: 44px; line-height: .86;
    color: var(--magenta); letter-spacing: -1px; text-transform: uppercase;
  }
  .cover-you {
    position: absolute; left: 218px; top: 322px;
    font-family: "Sacramento", cursive; font-size: 82px; line-height: 1; color: var(--amber);
  }
  .cover-credit { position: absolute; left: 268px; top: 432px; font-size: 12px; letter-spacing: .5px; }

  /* Inside spread */
  .essay { background: var(--paper); padding: 44px 34px; font-size: 7.2px; line-height: 1.5; }
  .essay p { margin-bottom: 9px; }
  .essay .quote {
    margin-top: 14px; padding: 0 10px; color: var(--magenta);
    font-weight: 700; font-size: 7.6px; text-align: center;
  }
  .reflection { background: var(--night); }
  .portrait-large {
    position: absolute; left: 40px; top: 20px; width: 330px; height: 360px;
    background:
      radial-gradient(circle at 52% 30%, rgba(214,25,138,.85) 0%, rgba(214,25,138,.55) 22%, rgba(214,25,138,0) 34%),
      radial-gradient(ellipse 55% 60% at 52% 55%, #6b6b6b 0%, #2a2a2a 50%, var(--night) 80%);
  }
  .reflection-text {
    position: absolute; left: 34px; right: 34px; top: 382px;
    color: var(--paper); font-size: 7.2px; line-height: 1.5; text-align: center; font-weight: 600;
  }
  .reflection-text p { margin-bottom: 8px; }
</style>
</head>
<body>

<section class="spread spread--outside">
  <article class="page back-cover">
    <div class="series">
      <div class="mini-cover" aria-label="Reduced front cover">
        <div class="mini-photo" role="img" aria-label="Leaping dancer in blue dress"></div>
        <div class="mini-title">There<br>Will<br>Only<br>Ever<br>Be<br>One</div>
        <div class="mini-you">you!</div>
      </div>
      <div>
        <p class="series-intro"><em>There Will Only Ever Be One You</em> is the 16th in a series of Labor Day essays inviting a moment of reflection on living a more meaningful, more mindful life</p>
        <div class="contact">
          <strong>Nora Ellery Vale, Ph.D.</strong><br>
          Linden Gate House · 12 Orchard Lane<br>
          Westbrook Hollow, Massachusetts 01900
          <div class="gap">Mobile: 555-014-2290<br>Email: nvale@example.net<br>©2023</div>
        </div>
      </div>
    </div>

    <div class="portrait-small" role="img" aria-label="Black and white photograph of Helena Brisk dancing"></div>

    <div class="about">
      <h3>About Helena Brisk:</h3>
      <p>Born in 1894, Helena Brisk danced and taught for over seventy years. She is recognized as a primal artistic force of the twentieth century, and her influence on modern art reaches well beyond the stage. Her themes drew on the lives and struggles of ordinary people, and she sought to reveal the depths of human emotion through movement that was fierce, angular and percussive, startlingly unlike the formality of classical ballet.</p>
      <h3>About photographer Clara Vance:</h3>
      <p>In 1935 Clara Vance saw a performance by Helena Brisk, and the two artists began a long collaboration. Inspired by the dancer's vision, Vance devoted herself to capturing movement in still images. Her photograph on this page is among the best known of the series, taken during a piece built around a poem.</p>
    </div>
  </article>

  <article class="page front-cover">
    <div class="dancer-photo" role="img" aria-label="Dancer in a flowing blue dress leaping mid-air, photo by Lumafold"></div>
    <h1 class="cover-title">There<br>Will<br>Only<br>Ever<br>Be<br>One</h1>
    <div class="cover-you">you!</div>
    <p class="cover-credit">Helena Brisk</p>
  </article>
</section>

<section class="spread spread--inside">
  <article class="page essay">
    <p>In the rural Ohio village where I grew up, one of the highlights of Sunday morning church service was the special music between the hymns and the sermon. One Sunday, a young soloist stepped to the pulpit, puckered up her lips and began to whistle. Despite the irreverence of my ten-year-old giggle, I found it an iconic example of someone daring to express herself in her own, truly authentic way.</p>
    <p>Someone who personified the irrepressible impulse to express her individuality was the early twentieth century dancer and choreographer Helena Brisk. She rejected the rigidly dictated forms of classical ballet and created a new language of dance, a revolutionary vocabulary of movement that electrified the stage.</p>
    <p>In her biography of Brisk, her friend and equally talented choreographer Iris Calder recalled that despite glowing reviews she had a gnawing feeling her own work was only mediocre. Brisk listened quietly and then responded:</p>
    <p class="quote">“There is a vitality, a life force, an energy, a quickening that is translated through you into action. And because there is only one of you in all of time, this expression is unique. If you block it, it will never exist through any other medium and it will be lost. Keep the channel open!”</p>
  </article>

  <article class="page reflection">
    <div class="portrait-large" role="img" aria-label="Black and white portrait of Helena Brisk with a magenta circle behind her head and hands raised"></div>
    <div class="reflection-text">
      <p>Brisk's wisdom reminds us that we must not hold back or judge our gifts. Although there may be moments when we doubt ourselves, our job is to be fearless and to keep the channel open.</p>
      <p>Guard the precious miracle of your own uniqueness. Find that home-sweet-home feeling where you feel you are your most authentic self. There will only ever be one you! And importantly, respect the differences of others. Our world would be a drab, boring place if we all only whistled one tune.</p>
    </div>
  </article>
</section>

</body>
</html>
```